Redesign of page from emergency manual

Please redesign this PDF to look better. Please don't include any stock photos. It must be legible. Making some words bold is probably a good idea.

Here are some things I like :

https://tarrowbooks.com.au/collections/frontpage/products/the-plk-v2-ebook

https://img-cd.vostramediafiles.com/qa-ejkwPLOTYY_SuCKbZNu411Qwgjv8YssPxEdzXN93hDkSRjLXK8WmfgbmrJW4ZZ3yUPK=w1052-h592-rw

```html
<!DOCTYPE html>
<html lang="en">
<head>
<meta charset="utf-8">
<title>Hypertension, Acute</title>
<link rel="stylesheet" href="https://fonts.googleapis.com/css2?family=Noto+Sans:ital,wght@0,400;0,700;0,800;1,400&display=swap">
<style>
  :root{
    --teal:#036b78;
    --aqua:#90d9e4;
    --side:#2a3a3f;
    --ink:#111;
    --white:#fff;
  }
  *{box-sizing:border-box;margin:0;padding:0}
  html,body{width:1200px;height:928px;overflow:hidden;background:var(--white)}
  body{font-family:"Noto Sans",Verdana,sans-serif;color:var(--ink);position:relative;letter-spacing:.45px}
  .page{position:relative;width:1200px;height:928px}

  .title-bar{position:absolute;left:54px;top:1px;width:1057px;height:54px;background:var(--teal);border-radius:8px}
  .title{position:absolute;left:15px;top:2px;color:var(--white);font-size:37px;font-weight:800;letter-spacing:1.4px}
  .tagline{position:absolute;left:594px;top:6px;width:455px;height:42px;background:var(--aqua);border-radius:7px;
    font-size:17.5px;font-weight:800;line-height:20px;text-align:center;padding-top:1px;color:#0a1a1d;letter-spacing:.9px}

  .side-tab{position:absolute;left:1143px;top:0;width:57px;height:928px;background:var(--side);color:var(--white)}
  .side-num{position:absolute;top:38px;width:100%;text-align:center;font-size:23px;font-weight:800}
  .side-title{position:absolute;left:4px;top:257px;writing-mode:vertical-rl;font-size:41px;font-weight:800;line-height:48px;white-space:nowrap;letter-spacing:.5px}
  .side-rev{position:absolute;left:16px;top:758px;writing-mode:vertical-rl;font-size:16px;line-height:22px;white-space:nowrap}

  .intro{position:absolute;left:50px;top:70px;width:630px;font-size:20px;line-height:26px}
  .intro .sq{position:absolute;left:4px;top:9px;width:7px;height:7px;background:var(--ink)}
  .intro p{margin-left:26px}
  .intro .dot{position:relative;margin-left:53px;margin-top:19px}
  .intro .dot::before{content:"•";position:absolute;left:-20px}
  .intro .dash{position:relative;margin-left:108px;margin-top:16px;white-space:nowrap}
  .intro .dash::before{content:"–";position:absolute;left:-26px}

  .bp-table{position:absolute;left:681px;top:82px;width:431px;border-collapse:collapse;font-size:18px;text-align:center}
  .bp-table th,.bp-table td{border:1.5px solid var(--ink)}
  .bp-table caption{background:var(--teal);color:var(--aqua);font-weight:800;font-size:19px;height:38px;line-height:36px;border:1.5px solid var(--ink);border-bottom:none}
  .bp-table th{height:33px;font-weight:800}
  .bp-table td{height:33px}

  .caution{position:absolute;left:50px;top:315px;width:1040px;font-size:20px;line-height:26px;padding-left:26px}
  .caution .star{position:absolute;left:0;font-weight:800}

  .drug-table{position:absolute;left:67px;top:409px;width:1057px;border-collapse:collapse;font-size:20px}
  .drug-table th,.drug-table td{border:1.5px solid var(--ink);vertical-align:top}
  .drug-table th{background:var(--teal);color:var(--aqua);font-size:20px;font-weight:800;height:46px;vertical-align:middle;padding-bottom:6px}
  .drug-table .action{width:238px;background:var(--aqua);padding:6px 10px;line-height:24px}
  .drug-table ul{list-style:none;padding:5px 0 0 38px}
  .drug-table li{position:relative;line-height:24px;margin-bottom:9px;white-space:nowrap}
  .drug-table li::before{content:"";position:absolute;left:-24px;top:7px;width:7px;height:7px;background:var(--teal)}
  .drug-name{font-weight:700}
  .r1{height:81px}.r2{height:112px}.r3{height:77px}.r4{height:45px}

  .diff{position:absolute;left:0;top:782px;width:1140px;font-size:20px;line-height:23px}
  .diff h2{position:absolute;left:69px;top:0;font-size:20px;font-weight:400;white-space:nowrap}
  .diff h2::before{content:"";position:absolute;left:-22px;top:9px;width:7px;height:7px;background:var(--teal)}
  .diff ul{position:absolute;top:35px;list-style:none}
  .diff li{position:relative;padding-left:17px;white-space:nowrap;margin-bottom:1px}
  .diff li::before{content:"•";position:absolute;left:0}
  .c1{left:83px}.c2{left:414px}.c3{left:750px}
</style>
</head>
<body>
<div class="page">
  <header class="title-bar">
    <h1 class="title">Hypertension, Acute</h1>
    <div class="tagline">Sustained high blood pressure refractory<br>to treating reversible causes</div>
  </header>

  <aside class="side-tab">
    <div class="side-num">12</div>
    <div class="side-title">Hypertension, Acute</div>
    <div class="side-rev">Revision Feb 2020</div>
  </aside>

  <section class="intro">
    <span class="sq"></span>
    <p>In pediatrics, hypertension is almost always treated by addressing likely causes such as <strong>light anesthesia</strong> or <strong>measurement error</strong>:</p>
    <p class="dot">Ensure correct <strong>BP cuff size</strong>: cuff bladder<br>width ~ 40% of limb circumference</p>
    <p class="dot" style="margin-top:17px">Ensure arterial line transducer is at <strong>level of heart</strong></p>
    <p class="dash">Consider placing arterial line if not already present</p>
  </section>

  <table class="bp-table">
    <caption>Hypertensive Blood Pressure Range*</caption>
    <tr><th>Age (yr)</th><th>Systolic</th><th>Diastolic</th></tr>
    <tr><td>newborn</td><td>&gt;97</td><td>&gt;70</td></tr>
    <tr><td>1-3</td><td>&gt;105</td><td>&gt;61</td></tr>
    <tr><td>4-12</td><td>&gt;113</td><td>&gt;86</td></tr>
  </table>

  <p class="caution"><span class="star">*</span><strong>CAUTION:</strong> Anti-hypertensive drugs are <strong>almost never needed</strong> for routine pediatric cases. These medications are used almost exclusively for specialized cardiac, neurosurgical, or endocrine (pheochromocytoma) cases. <strong>Consult an expert</strong> before use. Rule-out increased ICP.</p>

  <table class="drug-table">
    <tr><th>Action</th><th>Drug (IV Dosing)</th></tr>
    <tr class="r1"><td class="action">Direct smooth muscle relaxation</td>
      <td><ul><li><span class="drug-name">Sodium nitroprusside</span> 0.5-10 MICROgrams/kg/min</li><li><span class="drug-name">HydrALAZINE</span> 0.1-0.2 mg/kg (adult dose 5-10 mg)</li></ul></td></tr>
    <tr class="r2"><td class="action">β-Adrenergic<br>blockade</td>
      <td><ul><li><span class="drug-name">Esmolol</span>&nbsp; 100-500 MICROgrams/kg over 5 min, then<br>25-300 MICROgrams/kg/min</li><li><span class="drug-name">Labetalol</span> (also α effect) 0.2-1 mg/kg q 10 min;&nbsp; 0.4-3 mg/kg/<em>hour</em> (infusion)</li></ul></td></tr>
    <tr class="r3"><td class="action">Calcium channel blockade</td>
      <td><ul><li><span class="drug-name">niCARdapine</span>&nbsp; 0.5-5 MICROgrams/kg/min</li><li><span class="drug-name">Clevidipine</span>&nbsp; 0.5-3.5 MICROgrams/kg/min</li></ul></td></tr>
    <tr class="r4"><td class="action">D1-dopamine agonist</td>
      <td><ul><li><span class="drug-name">Fenoldopam</span>&nbsp; 0.2-0.8 MICROgrams/kg/min</li></ul></td></tr>
  </table>

  <section class="diff">
    <h2>Consider Differential (Partial):</h2>
    <ul class="c1"><li>Light anesthesia (consider<br>vaporizer or infusion pump<br>empty or malfunctioning)</li><li>Hypercarbia</li></ul>
    <ul class="c2"><li>Hypoxemia</li><li>Arterial line transducer too<br>low or BP cuff too small</li><li>Withdrawal (EtOH or opioid)</li></ul>
    <ul class="c3"><li>Thyroid Storm</li><li>Pheochromocytoma</li><li>Drug Error</li></ul>
  </section>
</div>
</body>
</html>
```